Clean Plinth Ads Banner Design For A Finance Company

Hi,
We're a UK based finance company and are looking for new banner ads to use on the Plinth Display Network.
We want the end product to stand out by using strong, minimal design - ideally starting from a dark theme, although I'm open to ideas.
The copy should read:
'Fast Bridging Loans From 0.39% PM'
Once we have these designs agreed, we are looking to replicate them for other products, changing only the text on each ad - for example, 'commercial mortgage service you can rely on' or 'development finance service you can rely on'.
The colours used on our website are the following:
Black - #040303
Orange - #f79124
White - #ffffff
Grey - #ffffff
Example ads that I like - https://www.brimcastle.com/wp-content/uploads/2021/07/plinth-display-ads-example-2-final.png.webp
2 - https://quendrahub.com/wp-content/uploads/2020/03/fbdd56ba3bd16c7a8debb13a411de786.jpg

```html
<!DOCTYPE html>
<html lang="en">
<head>
<meta charset="utf-8">
<title>Fast Bridging Loans – Kestrel Finance Limited</title>
<link rel="stylesheet" href="https://fonts.googleapis.com/css2?family=Montserrat:wght@500;600;800&display=swap">
<style>
  :root {
    --orange: #f7931e;
    --white: #ffffff;
    --ink: #040303;
    --photo-light: #d9dde3;
    --photo-mid: #8aa0bb;
    --photo-deep: #3f5d83;
  }
  * { box-sizing: border-box; margin: 0; padding: 0; }
  html, body {
    width: 1200px;
    height: 828px;
    overflow: hidden;
    background: var(--white);
  }
  .banner {
    position: relative;
    width: 1200px;
    height: 828px;
    background: var(--white);
    font-family: "Montserrat", sans-serif;
    overflow: hidden;
  }
  .top-band {
    position: absolute;
    left: 0; top: 0;
    width: 100%;
    height: 20px;
    background: var(--orange);
  }
  .lower-band {
    position: absolute;
    left: 0; top: 445px;
    width: 100%;
    height: 383px;
    background: var(--orange);
  }
  .headline {
    position: absolute;
    left: 58px;
    top: 62px;
    color: var(--orange);
    font-weight: 500;
    font-size: 72px;
    line-height: 92px;
    letter-spacing: 0.5px;
  }
  .headline .rate {
    font-weight: 800;
  }
  .brand {
    position: absolute;
    left: 58px;
    top: 318px;
    display: flex;
    align-items: center;
    gap: 14px;
  }
  .brand-dot {
    width: 34px;
    height: 34px;
    border-radius: 50%;
    background: var(--orange);
  }
  .brand-name {
    color: var(--orange);
    font-weight: 600;
    font-size: 30px;
    line-height: 1.1;
    width: 220px;
  }
  .photo-couple {
    position: absolute;
    left: 414px;
    top: 280px;
    width: 662px;
    height: 518px;
    border-radius: 140px 140px 40px 40px;
    background: linear-gradient(170deg, var(--photo-light) 0%, var(--photo-mid) 45%, var(--photo-deep) 100%);
  }
</style>
</head>
<body>
  <main class="banner">
    <div class="top-band"></div>
    <div class="lower-band"></div>

    <h1 class="headline">
      Fast Bridging Loans<br>
      From <span class="rate">0.39% PM</span>
    </h1>

    <div class="brand">
      <span class="brand-dot"></span>
      <span class="brand-name">Kestrel Finance Limited</span>
    </div>

    <div class="photo-couple" role="img" aria-label="Photo of a smiling young couple in denim sitting together on the floor, looking upward"></div>
  </main>
</body>
</html>
```